Product label for specialty fertilizer for cannabis

Create a label with our brand name and product information. The name of the new product is “Dravel” and the name is also the logo. The color palate is white/platinium/silver/shimmery. The product makes the flowers dense and hard so we want the logo to look strong and masculine. The liquid inside the bottle is white Which is what dravel means in Spanish
Also need a font for all the product information. See pics for example and
Target Market(s)
Cannabis growers
Industry/Entity Type
Cannabis
Colors
Designer to choose colors to be used in the design.
Requirements
Must have
- Strong visual presence for retail environment. Clean but bold look.
Nice to have
- Would be nice to have similar to a Fizzo Brava font
Should not have
- Do not put any cannabis or marijuana images anywhere on the label

```html
<!DOCTYPE html>
<html lang="en">
<head>
<meta charset="UTF-8">
<title>Dravel – Fertilizer Label</title>
<link href="https://fonts.googleapis.com/css2?family=Arimo:wght@400;700&family=Bodoni+Moda:wght@500&display=swap" rel="stylesheet">
<style>
  :root {
    --bg: #1d1d1e;
    --bg-light: #262627;
    --white: #f4f4f4;
    --silver: #c9c9cf;
    --grey-text: #8d8d8f;
    --faint: rgba(255,255,255,0.06);
  }
  * { box-sizing: border-box; margin: 0; padding: 0; }
  html, body { width: 1200px; height: 600px; overflow: hidden; background: var(--bg); }
  body { font-family: "Arimo", Arial, sans-serif; color: var(--white); }

  .label {
    position: relative;
    width: 1200px; height: 600px; overflow: hidden;
    background: radial-gradient(ellipse at 50% 45%, var(--bg-light) 0%, var(--bg) 70%);
  }

  .edge-strip {
    position: absolute; top: 0; width: 22px; height: 600px;
    background: repeating-linear-gradient(180deg, #d8d8dc 0 7px, #6b6b70 7px 10px, transparent 10px 33px);
    opacity: .85;
  }
  .edge-strip--left { left: 0; }
  .edge-strip--right { right: 0; }

  /* left panel */
  .brand-box {
    position: absolute; left: 32px; top: 55px; width: 95px; height: 103px;
    background: #0c0c0c; border: 2px solid var(--white); outline: 1px solid #0c0c0c; outline-offset: -5px;
    display: flex; align-items: center; justify-content: center;
    font-family: "Bodoni Moda", serif; font-weight: 500; font-size: 17px; color: var(--white);
    letter-spacing: 1px;
  }
  .brand-title {
    position: absolute; left: 137px; top: 50px;
    font-family: "Bodoni Moda", serif; font-weight: 500; font-size: 15px; letter-spacing: 3.5px;
  }
  .brand-intro {
    position: absolute; left: 137px; top: 71px; width: 177px;
    font-size: 10.2px; line-height: 12px; text-align: justify; color: var(--white);
  }
  .copy {
    position: absolute; font-size: 9.4px; line-height: 12px; color: var(--grey-text);
    text-align: justify; hyphens: auto;
  }
  .copy p + p { margin-top: 13px; }
  .copy--left { left: 35px; top: 167px; width: 279px; }
  .copy--right { left: 912px; top: 127px; width: 256px; }

  .warning { position: absolute; left: 34px; top: 496px; }
  .warning__icon { position: absolute; left: 0; top: 0; }
  .warning__text { position: absolute; left: 75px; top: 5px; width: 220px; }
  .warning__title { font-weight: 700; font-size: 15px; line-height: 16px; }
  .warning__sub { font-weight: 700; font-size: 9.6px; line-height: 12px; }
  .warning__note { font-size: 9.4px; line-height: 12px; color: var(--grey-text); }

  .divider { position: absolute; top: 36px; }
  .divider--left { left: 317px; }
  .divider--right { left: 883px; }

  /* centre */
  .emblem { position: absolute; left: 0; top: 0; }
  .logo-name {
    position: absolute; left: 0; width: 1224px; top: 215px; text-align: center;
    font-family: "Bodoni Moda", serif; font-weight: 500; font-size: 128px; line-height: 150px;
    color: var(--white);
  }
  .established {
    position: absolute; left: 564px; top: 382px; width: 120px; text-align: center;
    font-family: "Bodoni Moda", serif; font-weight: 500; font-size: 15px; letter-spacing: 3px;
    border-top: 1px solid #9a9a9e; border-bottom: 1px solid #9a9a9e; padding: 2px 0 1px;
  }
  .net-weight {
    position: absolute; left: 0; width: 1226px; top: 539px; text-align: center;
    font-weight: 700; font-size: 15px; letter-spacing: 1.8px;
  }

  /* right panel */
  .faint-name {
    position: absolute; left: 905px; top: -28px;
    font-family: "Bodoni Moda", serif; font-weight: 500; font-size: 100px; color: var(--faint);
  }
  .directions {
    position: absolute; right: 37px; top: 89px; text-align: right;
    font-weight: 700; font-size: 13px; line-height: 18px;
  }
  .directions__title { margin-right: 31px; }
  .maker { position: absolute; left: 926px; top: 523px; }
  .maker__title { font-weight: 700; font-size: 13.5px; line-height: 16px; }
  .maker__line { font-size: 9.8px; line-height: 12px; }
</style>
</head>
<body>
<main class="label">
  <div class="edge-strip edge-strip--left" role="img" aria-label="Decorative silver binding pattern along the left edge"></div>
  <div class="edge-strip edge-strip--right" role="img" aria-label="Decorative silver binding pattern along the right edge"></div>

  <!-- left panel -->
  <div class="brand-box">DRAVEL</div>
  <h2 class="brand-title">DRAVEL</h2>
  <p class="brand-intro">Lorem Ipsum is simply dummy text of the printing and typesetting industry. Lorem Ipsum has been the industry's standard dummy text ever since the 1500s, when an unknown printer took a galley of type and scrambled it to make a type specimen book. It has L</p>

  <div class="copy copy--left">
    <p>Lorem Ipsum is simply dummy text of the printing and typesetting industry. Lorem Ipsum has been the industry's standard dummy text ever since the 1500s, when an unknown printer took a galley of type and scrambled it to make a type specimen book. It has survived not only five centuries, but also the leap into electronic typesetting, remaining essentially unchanged. It was popularised in the 1960s with the release of Transferly sheets containing Lorem Ipsum passages, and more recently with desktop publishing software like Quillset Layout including versions of Lorem Ipsum.</p>
    <p>Lorem Ipsum is simply dummy text of the printing and typesetting industry. Lorem Ipsum has been the industry's standard dummy text ever since the 1500s, when an unknown printer took a galley of type and scrambled it to make a type specimen book. It has survived not only five centuries, but also the leap into electronic typesetting, remaining essentially unchanged. It was popularised in the 1960s with the release of Transferly sheets containing Lorem Ipsum passages, and more recently with desktop publishing software like Quillset Layout including versions of Lorem Ipsum.</p>
    <p>Lorem Ipsum is simply dummy text of the printing and typesetting industry. Lorem Ipsum has been the industry's standard dummy text ever since the 1500s, when an unknown printer took a galley of type and scrambled it to make a type specimen book.</p>
  </div>

  <div class="warning">
    <svg class="warning__icon" width="66" height="66" viewBox="0 0 66 66">
      <rect x="12" y="12" width="42" height="42" transform="rotate(45 33 33)" fill="#f4f4f4"/>
      <rect x="30" y="17" width="6" height="22" fill="#1d1d1e"/>
      <rect x="30" y="43" width="6" height="6" fill="#1d1d1e"/>
    </svg>
    <div class="warning__text">
      <p class="warning__title">WARNING:</p>
      <p class="warning__sub">KEEP OUT OF REACH OF CHILDREN</p>
      <p class="warning__note">Plant fertilizers can poison people and pets<br>if they are inhaled or accidentally ingested.</p>
    </div>
  </div>

  <svg class="divider divider--left" width="20" height="534" viewBox="0 0 20 534">
    <line x1="10" y1="10" x2="10" y2="524" stroke="#e8e8e8" stroke-width="1.4"/>
    <path d="M10 0 L12 8 L20 10 L12 12 L10 20 L8 12 L0 10 L8 8 Z" fill="#f4f4f4"/>
    <path d="M10 514 L12 522 L20 524 L12 526 L10 534 L8 526 L0 524 L8 522 Z" fill="#f4f4f4"/>
    <circle cx="10" cy="24" r="3.5" fill="#f4f4f4"/>
    <circle cx="10" cy="267" r="3.5" fill="#f4f4f4"/>
    <circle cx="10" cy="510" r="3.5" fill="#f4f4f4"/>
  </svg>
  <svg class="divider divider--right" width="20" height="534" viewBox="0 0 20 534">
    <line x1="10" y1="10" x2="10" y2="524" stroke="#e8e8e8" stroke-width="1.4"/>
    <path d="M10 0 L12 8 L20 10 L12 12 L10 20 L8 12 L0 10 L8 8 Z" fill="#f4f4f4"/>
    <path d="M10 514 L12 522 L20 524 L12 526 L10 534 L8 526 L0 524 L8 522 Z" fill="#f4f4f4"/>
    <circle cx="10" cy="24" r="3.5" fill="#f4f4f4"/>
    <circle cx="10" cy="267" r="3.5" fill="#f4f4f4"/>
    <circle cx="10" cy="510" r="3.5" fill="#f4f4f4"/>
  </svg>

  <!-- centre emblem -->
  <svg class="emblem" width="1200" height="600" viewBox="0 0 1200 600" fill="none">
    <path d="M422 208 A205 205 0 0 1 808 218" stroke="#a9a9b0" stroke-width="3"/>
    <path d="M445 218 A185 185 0 0 1 784 232" stroke="#f4f4f4" stroke-width="3"/>
    <path d="M790 402 A205 205 0 0 1 450 420" stroke="#a9a9b0" stroke-width="3"/>
    <path d="M764 386 A185 185 0 0 1 472 400" stroke="#f4f4f4" stroke-width="3"/>
  </svg>
  <h1 class="logo-name">Dravel</h1>
  <p class="established">EST. 2022</p>
  <p class="net-weight">NET WT. 24 OZ. (1.5LB) 680 G</p>

  <!-- right panel -->
  <p class="faint-name" aria-hidden="true">Dravel</p>
  <div class="directions">
    <p class="directions__title">DIRECTIONS:</p>
    <p>SHAKE WELL BEFORE USE</p>
  </div>
  <div class="copy copy--right">
    <p>Lorem Ipsum is simply dummy text of the printing and typesetting industry. Lorem Ipsum has been the industry's standard dummy text ever since the 1500s, when an unknown printer took a galley of type and scrambled it to make a type specimen book. It has survived not only five centuries, but also the leap into electronic typesetting, remaining essentially unchanged. It was popularised in the 1960s with the release of Transferly sheets containing Lorem Ipsum passages, and more recently with desktop publishing software like Quillset Layout including versions of Lorem Ipsum.</p>
    <p>Lorem Ipsum is simply dummy text of the printing and typesetting industry. Lorem Ipsum has been the industry's standard dummy text ever since the 1500s, when an unknown printer took a galley of type and scrambled it to make a type specimen book. It has survived not only five centuries, but also the leap into electronic typesetting, remaining essentially unchanged. It was popularised in the 1960s with the release of Transferly sheets containing Lorem Ipsum passages, and more recently with desktop publishing software like Quillset Layout including versions of Lorem Ipsum.</p>
    <p>Lorem Ipsum is simply dummy text of the printing and typesetting industry. Lorem Ipsum has been the industry's standard dummy text ever since the 1500s, when an unknown printer took a galley of type and scrambled it to make a type specimen book.</p>
  </div>

  <div class="maker">
    <p class="maker__title">MANUFACTURED BY:</p>
    <p class="maker__line"><strong>DRAVEL FARMS</strong>, SOMETHING RD. CA, 9061</p>
    <p class="maker__line">www. dravelfertilizers.com</p>
  </div>
</main>
</body>
</html>
```